Aerospace Distributor & Repair Station
New Web site
Thank you to all
we have selected design 59 from Pixmorra
we have a new contest please check it out
Thanks
Sorry Everybody, I am out of the office during the labor day holiday.
I will post the winner tomorrow when I get back to the office
Thank you for your Participation
All the best
Hi All
We have extended the contest due to the unavailability of the Executive team to meet
we should have a final answer by monday
Thank you for your patience
Dear All
We will provide fedback to each designer that we have liked the designs for a final approval
Please provide New designs, idea's, concepts Do not copy existing desdigns
Appreciate everybody's work
Hello PH,
Please download the drafts for better quality. Thanks. :)
Thank you for submitting your Designs
We have rated each design so far, do not withdraw your designs yet if you have gotten a low star rating.
we will submit all designs to the executive team for a final decision
also Designers that have not submitted yet please do so as soon as possible before submittal to executive team
Appreciate your work
best regards
thanks,
BrightCraftStudio
To Quobant
Thank you for the submittal
I would like to see more dynamic curves instead of all square design and more sophisticated
I understand that there will be no flash or images moving at the template design level
Looking forward for additionnal designs
thanks
"dislikes : simple picture with no graphic, Block design"
Just a point, what we show in there is image type file to you see/choose the best of the best.
So, you will not see images moving, like would be in an movie flash. So please, think better, because you will need to choose the template by the conception of the design you like and reply to us please and qualify with the stars please.
Obs: I will start sending mines.
Regards,
Hello All
Thank you for all comments
Please provide PSD for Home page and if possible will accept HTML, will be plus
We have uploaded pictures which we have rights on as well variation of LOGO
Please let us know if you require additionnal information
All the Best
please advise on the following logo web page mock-ups are just a psd or html / asp / php
Yes, just because we there do templates for PSD file type, but I also can do html and code all pages.
Hi,
i have the same question as Quobant, do you only need the PSD or do you also need it to be converted to html?
PH, I checked you Additional comments and I want to know. You want html files ? Regards.
Just a note: The sides of the page, do not go see like seems. Will have small margin, but as we all use different types of screens to be seen just drew equally to all. Please note that you will see as see any other site. I give you certainly ulpoading an image to you see how works in the browser. Regards

```html
<!DOCTYPE html>
<html lang="en">
<head>
<meta charset="utf-8">
<title>K7 Globalia, LLC — Contact Us</title>
<link href="https://fonts.googleapis.com/css2?family=Arimo:ital,wght@0,400;0,700;1,400&display=swap" rel="stylesheet">
<style>
:root{
  --stage:#0c0b10;
  --panel:#ffffff;
  --ink:#333333;
  --muted:#6d6d6d;
  --label:#555555;
  --navy:#0d1f5c;
  --navy-deep:#06113a;
  --navy-light:#1f3a8f;
  --link:#1d3f8c;
  --field:#ececec;
  --field-line:#d2d2d2;
  --side-head:#d9d9d9;
  --foot:#f1f1f1;
  --rule:#cfcfcf;
}
*{box-sizing:border-box;margin:0;padding:0}
html,body{width:1200px;height:828px;overflow:hidden}
body{font-family:"Arimo",Arial,sans-serif;color:var(--ink);position:relative;
  background:var(--stage)}
.backdrop{position:absolute;inset:0;
  background:
   radial-gradient(circle at 8% 20%,rgba(150,40,120,.45),transparent 22%),
   radial-gradient(circle at 92% 18%,rgba(40,90,170,.4),transparent 20%),
   radial-gradient(circle at 12% 75%,rgba(60,130,90,.35),transparent 20%),
   radial-gradient(circle at 88% 78%,rgba(170,60,60,.35),transparent 22%),
   var(--stage)}
.page{position:absolute;left:240px;top:29px;width:720px;height:766px;background:var(--panel);
  border-radius:6px;overflow:hidden;box-shadow:0 0 30px rgba(0,0,0,.6)}
.abs{position:absolute}
.phone-tab{left:576px;top:5px;width:137px;height:19px;background:#dcdcdc;border-radius:0 0 4px 4px;
  font-size:11px;color:#fff;text-align:right;padding:3px 10px 0 0;background:linear-gradient(#c9c9c9,#b3b3b3)}
.brand{left:31px;top:13px;font-size:22px;font-weight:700;color:#333;letter-spacing:.5px}
.tagline{left:31px;top:42px;font-size:10px;color:#888}
.nav{left:319px;top:40px;display:flex;gap:0;font-size:9px;color:#444;text-transform:uppercase}
.nav span{position:absolute;top:0;white-space:nowrap}
.nav .current{background:var(--navy-light);color:#fff;padding:3px 8px;top:-4px;border-radius:2px}
.banner{left:0;top:77px;width:720px;height:52px;
  background:linear-gradient(180deg,var(--navy-light) 0%,var(--navy) 45%,var(--navy-deep) 100%)}
.banner h1{position:absolute;left:31px;top:13px;font-size:20px;color:#fff;font-weight:700}
.banner p{position:absolute;left:221px;top:17px;font-size:14px;font-style:italic;color:#fff}
.field{position:absolute}
.field label{display:block;font-size:10px;color:var(--label);margin-bottom:3px}
.field .box{width:288px;height:18px;background:var(--field);border:1px solid var(--field-line);border-radius:2px}
.field .area{height:100px}
.submit{left:43px;top:537px;width:55px;height:15px;font-size:8px;color:#555;text-align:center;
  background:linear-gradient(#fafafa,#dcdcdc);border:1px solid #bbb;border-radius:2px;padding-top:2px}
.side{left:528px;width:192px}
.side h3{background:var(--side-head);font-size:11px;font-weight:700;padding:5px 10px;color:#333}
.side p{font-size:8px;line-height:12px;color:#555;padding:6px 14px}
.social{display:flex;gap:10px;padding:12px 17px}
.social span{width:24px;height:24px;background:#2b2b2b;border-radius:3px}
.footer{left:0;top:561px;width:720px;height:173px;background:var(--foot);border-top:1px solid var(--rule)}
.col{position:absolute;top:12px}
.col h4{font-size:11px;color:var(--link);margin-bottom:6px}
.col p,.col li{font-size:8px;line-height:12px;color:#555;list-style:none}
.bottom{left:0;top:734px;width:720px;height:32px;background:#fff;border-top:1px solid var(--rule);
  font-size:8px;color:#555}
.bottom .copy{position:absolute;left:31px;top:11px}
.bottom .legal{position:absolute;right:30px;top:11px}
</style>
</head>
<body>
<div class="backdrop" role="img" aria-label="Dark background with soft blurred coloured light spots"></div>
<main class="page">
  <div class="abs phone-tab">(555) 014-2290</div>
  <div class="abs brand">K7 GLOBALIA, LLC</div>
  <div class="abs tagline">Aerospace Distributor &amp; Repair Station</div>
  <nav class="abs nav">
    <span style="left:0">Home</span>
    <span style="left:70px">About Us</span>
    <span style="left:154px">Services</span>
    <span style="left:240px">Our Portal</span>
    <span class="current" style="left:316px">Contact</span>
  </nav>
  <header class="abs banner">
    <h1>Contact Us</h1>
    <p>Please fill out the following form and a representative will contact you.</p>
  </header>

  <form>
    <div class="field" style="left:31px;top:141px"><label>*Name:</label><div class="box"></div></div>
    <div class="field" style="left:31px;top:179px"><label>Title:</label><div class="box"></div></div>
    <div class="field" style="left:31px;top:218px"><label>Address:</label><div class="box"></div></div>
    <div class="field" style="left:31px;top:254px"><label>Postal Code:</label><div class="box"></div></div>
    <div class="field" style="left:31px;top:292px"><label>Country:</label><div class="box"></div></div>
    <div class="field" style="left:31px;top:328px"><label>Email:</label><div class="box"></div></div>
    <div class="field" style="left:31px;top:366px"><label>*Tel:</label><div class="box"></div></div>
    <div class="field" style="left:31px;top:414px"><label>Message:</label><div class="box area"></div></div>
    <div class="abs submit">SUBMIT</div>
    <div class="field" style="left:396px;top:141px"><label>*Company:</label><div class="box"></div></div>
    <div class="field" style="left:396px;top:179px"><label>City:</label><div class="box"></div></div>
    <div class="field" style="left:396px;top:218px"><label>State:</label><div class="box"></div></div>
  </form>

  <aside class="abs side" style="top:285px">
    <h3>Company Info</h3>
    <p>K7 Globalia, LLC<br>4820 W Harbor Ln<br>Brookvale, WI 53990<br>USA<br>Tel: (555) 014-2290<br>Fax: (555) 014-2291</p>
    <h3 style="margin-top:4px">Contact Details</h3>
    <p>Phone: (555) 014-2290<br>Website: www.k7globalia.com<br>Cage Code: 9QX72</p>
    <h3 style="margin-top:4px">Connect With Us</h3>
    <div class="social" role="img" aria-label="Social network links"><span></span><span></span><span></span></div>
  </aside>

  <footer class="abs footer">
    <div class="col" style="left:31px;width:150px">
      <h4>Browse Site</h4>
      <ul><li>About our company</li><li>Contact us</li><li>Our Services</li><li>Client Testimonials</li></ul>
    </div>
    <div class="col" style="left:202px;width:250px">
      <h4>Our Costumers</h4>
      <p>We believe that our customer is our number one priority and are committed to meeting or exceeding our customer's requirements by providing superior customer service and innovative solutions for the best value. We are continuously looking for methods to improve our operations and pass along cost savings to our customers without affecting the quality of our products and services.</p>
    </div>
    <div class="col" style="left:480px;width:212px">
      <h4>Our Portal</h4>
      <p>Please use the system and information on it responsibly. Unauthorized access or use is prohibited, and subject to discipline, civil and criminal prosecution. By using this system, you consent to K7 Globalia storing data internally about any access, use, information and communications on this system. You acknowledge that your use and information on, and usage of, this system may be monitored, recorded, retrieved and disclosed to others. You also agree to abide by all K7 Globalia policies for proper system use, and the protection of sensitive and export controlled data.</p>
    </div>
  </footer>
  <div class="abs bottom">
    <span class="copy">Copyright © 2011, All rights reserved. K7Globalia.com</span>
    <span class="legal">TERMS &amp; CONDITIONS | PRIVACY &amp; POLICY</span>
  </div>
</main>
</body>
</html>
```